Business Card Design

Im a small business that specialises in all aspects of sign installation, big and small, domestic and commercial. I have a construction and carpentry background. I'm after a professional looking business card, that has my logo as the forefront of the card incorporating the same colours as the my logo. No slogan as yet, but open to suggestions. The final design should communicate quality and class workmanship.

Target Market(s)

Managers and Owners of businesses

Industry/Entity Type

Small Business

Contact Information for Business Card

Carwyn Solbeck
Mob: 0417295036
Email: kto.fitouts@quillmail.net

Sign Installation
Property Improvement and Maintenance
Trade Services

Colors
dbdbdb
000000
ffffff

Requirements
Must have
• Logo
My name
My contact details
What I specialise in
Nice to have
• background image/images that are only just noticeable and do not take away from the logo or text.
Should not have
• No colours that contrast from my logo
No heavy machinery images to be used
Logo must stand out

```html
<!DOCTYPE html>
<html lang="en">
<head>
<meta charset="utf-8">
<title>KTO Installations – Business Card</title>
<link href="https://fonts.googleapis.com/css2?family=Open+Sans:wght@600;700&display=swap" rel="stylesheet">
<style>
  :root {
    --page: #ffffff;
    --brand-blue: #2a4c9e;
    --navy-deep: #1e2033;
    --navy-mid: #253f8f;
    --silver-dark: #bfc0c3;
    --silver-mid: #e6e7e8;
    --silver-light: #ffffff;
    --ink-white: #ffffff;
  }
  * { margin: 0; padding: 0; box-sizing: border-box; }
  html, body {
    width: 1022px; height: 1200px; overflow: hidden;
    background: var(--page);
    font-family: "Open Sans", Arial, sans-serif;
  }
  .canvas { position: relative; width: 1022px; height: 1200px; }

  .card {
    position: absolute;
    width: 707px; height: 410px;
    overflow: hidden;
    background: linear-gradient(90deg, var(--silver-dark) 0%, #f1f1f2 28%, var(--silver-light) 50%, var(--silver-mid) 78%, var(--silver-dark) 100%);
    box-shadow: 0 4px 14px rgba(0,0,0,0.22);
  }
  .card--front { left: 118px; top: 123px; }
  .card--back  { left: 119px; top: 576px; width: 708px; }

  .card__bands { position: absolute; inset: 0; width: 100%; height: 100%; }

  /* Front: company name lockup */
  .brand {
    position: absolute; left: 132px; top: 88px;
    display: flex; align-items: center; gap: 22px;
  }
  .brand__dot {
    width: 104px; height: 104px; border-radius: 50%;
    background: var(--brand-blue);
  }
  .brand__name {
    font-weight: 700; font-size: 44px; line-height: 1;
    color: var(--brand-blue); letter-spacing: 0.5px;
  }

  .services {
    position: absolute; left: 190px; top: 286px;
    list-style: none;
  }
  .services__item {
    display: flex; align-items: center; gap: 20px;
    height: 36px;
    color: var(--ink-white); font-weight: 600; font-size: 21px;
  }
  .services__bullet {
    width: 12px; height: 12px; border-radius: 50%;
    background: var(--ink-white); margin-left: 6px;
  }

  /* Back: name and contact */
  .holder-name {
    position: absolute; left: 0; right: 0; top: 70px;
    text-align: center;
    color: var(--ink-white); font-weight: 700; font-size: 32px;
  }
  .contact {
    position: absolute; left: 0; right: 0; top: 242px;
    display: flex; flex-direction: column; align-items: center; gap: 14px;
    color: var(--brand-blue); font-weight: 700; font-size: 22px;
  }
  .contact__line { display: flex; align-items: center; gap: 10px; line-height: 30px; }
  .contact__icon { width: 28px; height: 24px; }
</style>
</head>
<body>
<main class="canvas">

  <section class="card card--front" aria-label="Card front">
    <svg class="card__bands" viewBox="0 0 707 410" preserveAspectRatio="none" aria-hidden="true">
      <defs>
        <linearGradient id="frontBand" x1="0" y1="0" x2="0" y2="1">
          <stop offset="0" stop-color="#2b4a9b"/>
          <stop offset="1" stop-color="#1d1f33"/>
        </linearGradient>
        <linearGradient id="frontRail" x1="0" y1="0" x2="1" y2="0">
          <stop offset="0" stop-color="#9c9da0"/>
          <stop offset="0.5" stop-color="#ffffff"/>
          <stop offset="1" stop-color="#8f9093"/>
        </linearGradient>
      </defs>
      <path d="M0 268 Q353 244 707 272 L707 286 Q353 256 0 284 Z" fill="url(#frontRail)"/>
      <path d="M0 284 Q353 256 707 286 L707 410 L0 410 Z" fill="url(#frontBand)"/>
    </svg>

    <div class="brand">
      <span class="brand__dot" aria-hidden="true"></span>
      <span class="brand__name">KTO Installations</span>
    </div>

    <ul class="services">
      <li class="services__item"><span class="services__bullet"></span>Sign Installation</li>
      <li class="services__item"><span class="services__bullet"></span>Property Improvement</li>
      <li class="services__item"><span class="services__bullet"></span>Maintenance Trade Services</li>
    </ul>
  </section>

  <section class="card card--back" aria-label="Card back">
    <svg class="card__bands" viewBox="0 0 708 410" preserveAspectRatio="none" aria-hidden="true">
      <defs>
        <linearGradient id="backBand" x1="0" y1="0" x2="0" y2="1">
          <stop offset="0" stop-color="#1f2030"/>
          <stop offset="1" stop-color="#27439a"/>
        </linearGradient>
        <linearGradient id="backRail" x1="0" y1="0" x2="1" y2="0">
          <stop offset="0" stop-color="#9c9da0"/>
          <stop offset="0.5" stop-color="#ffffff"/>
          <stop offset="1" stop-color="#8f9093"/>
        </linearGradient>
      </defs>
      <path d="M0 126 Q354 150 708 124 L708 134 Q354 162 0 140 Z" fill="url(#backRail)"/>
      <path d="M0 0 H708 V124 Q354 150 0 126 Z" fill="url(#backBand)"/>
    </svg>

    <h1 class="holder-name">Carwyn Solbeck</h1>

    <div class="contact">
      <p class="contact__line">
        <svg class="contact__icon" viewBox="0 0 28 24" aria-hidden="true">
          <rect x="7" y="1.5" width="14" height="21" rx="2.5" fill="none" stroke="currentColor" stroke-width="2"/>
          <line x1="12" y1="19" x2="16" y2="19" stroke="currentColor" stroke-width="1.6"/>
        </svg>
        0417295036
      </p>
      <p class="contact__line">
        <svg class="contact__icon" viewBox="0 0 28 24" aria-hidden="true">
          <rect x="1.5" y="4" width="25" height="16" rx="1.5" fill="none" stroke="currentColor" stroke-width="2"/>
          <path d="M2 5 L14 14 L26 5" fill="none" stroke="currentColor" stroke-width="2"/>
        </svg>
        kto.fitouts@quillmail.net
      </p>
    </div>
  </section>

</main>
</body>
</html>
```